Flyer for Aluminium recycling business

We are a startup aluminium recycling business. We don’t have a logo yet. I’ve attached a flyer created by one of our sales people but it’s a bit average and we need something a bit more modern and slick. You have creative license to completely change everything - as long as the information being communicated is the same.

Target Market(s)

Hospitality, Hotels, Apartment blocks, malls etcs

Industry/Entity Type

Aluminium recycling

Requirements
Must have
• the wording
Nice to have
• you have free license on design aspect

```html
<!DOCTYPE html>
<html lang="en">
<head>
<meta charset="utf-8">
<title>Brightloop Co. – Aluminium Recycling Flyer</title>
<link rel="stylesheet" href="https://fonts.googleapis.com/css2?family=Poppins:wght@400;500;600;700;800&display=swap">
<style>
  :root {
    --mat: #b7b7b9;
    --paper: #ffffff;
    --forest: #1a5c32;
    --leaf: #22b14c;
    --ink: #111111;
    --white: #ffffff;
  }
  * { margin: 0; padding: 0; box-sizing: border-box; }
  html, body {
    width: 982px; height: 1200px; overflow: hidden;
    background: var(--mat);
    font-family: "Poppins", sans-serif;
    color: var(--ink);
  }
  .flyer {
    position: absolute; left: 134px; top: 95px;
    width: 714px; height: 1010px;
    background: var(--paper);
    overflow: hidden;
  }
  .hero-band {
    position: absolute; left: 0; top: 0;
    width: 714px; height: 266px;
    background: var(--forest);
  }
  .hero-photo { position: absolute; left: 0; top: 0; }
  .headline {
    position: absolute; left: 42px; top: 25px;
    font-size: 36.5px; font-weight: 600; line-height: 44px;
    color: var(--white); letter-spacing: -0.2px;
    white-space: nowrap;
  }
  .headline .accent { color: var(--leaf); font-weight: 700; }
  .tagline {
    position: absolute; left: 39px; top: 163px;
    font-size: 18.5px; font-weight: 600; line-height: 23px;
    color: var(--white);
  }
  .brand {
    position: absolute; left: 474px; top: 72px; width: 240px;
    display: flex; align-items: center; justify-content: center; gap: 8px;
  }
  .brand-dot {
    width: 16px; height: 16px; border-radius: 50%;
    background: var(--forest); flex: none;
  }
  .brand-name {
    font-size: 22px; font-weight: 600; line-height: 26px;
    color: var(--ink); white-space: nowrap;
  }
  .section-title {
    position: absolute; left: 40px; top: 302px;
    font-size: 37px; font-weight: 700; color: var(--leaf);
    letter-spacing: -0.5px;
  }
  .list-heading {
    position: absolute; left: 42px;
    font-size: 16px; font-weight: 700; color: var(--ink);
  }
  .checklist {
    position: absolute; left: 42px; width: 640px;
    list-style: none;
    font-size: 14.5px; font-weight: 400; line-height: 17.5px;
  }
  .checklist li { position: relative; padding-left: 17px; }
  .checklist .tick {
    position: absolute; left: 0; top: 3px; width: 12px; height: 12px;
  }
  .steps { top: 397px; }
  .steps li { margin-bottom: 7px; }
  .materials { top: 609px; }
  .materials li { margin-bottom: 4.5px; }
  .gallery {
    position: absolute; left: 42px; top: 743px;
    display: flex; gap: 16px;
  }
  .gallery-tile {
    width: 144px; height: 144px;
    border: 7px solid var(--leaf); border-radius: 8px;
    overflow: hidden;
  }
  .tile-scrap { background: linear-gradient(180deg, #6f8fb8 0%, #8a8e93 30%, #4c4f53 100%); }
  .tile-cans { background: linear-gradient(135deg, #b9bfc2 0%, #5f8a5a 35%, #d4b23a 55%, #b7473f 75%, #7c8589 100%); }
  .tile-trays { background: radial-gradient(ellipse at 50% 55%, #c9cccf 0%, #e6e7e9 45%, #ffffff 75%); }
  .tile-caps { background: linear-gradient(135deg, #2f6b3a 0%, #e15a2c 30%, #3bb8b0 50%, #c8304a 70%, #5a4fc8 100%); }
  .footer-wave { position: absolute; left: 0; top: 880px; }
  .call-label {
    position: absolute; left: 43px; top: 927px;
    font-size: 16px; font-weight: 700; color: var(--leaf);
  }
  .call-number {
    position: absolute; left: 43px; top: 944px;
    font-size: 20px; font-weight: 700; color: var(--ink);
  }
  .email {
    position: absolute; right: 47px; top: 945px;
    font-size: 15px; font-weight: 500; color: var(--white);
  }
</style>
</head>
<body>
<svg width="0" height="0" style="position:absolute">
  <symbol id="tick" viewBox="0 0 24 24">
    <path d="M21 11.1V12a9 9 0 1 1-5.3-8.2" fill="none" stroke="#22b14c" stroke-width="2.6" stroke-linecap="round"/>
    <path d="M8 11.5l3.5 3.5L22 4.5" fill="none" stroke="#22b14c" stroke-width="2.6" stroke-linecap="round" stroke-linejoin="round"/>
  </symbol>
</svg>

<main class="flyer">
  <div class="hero-band"></div>
  <svg class="hero-photo" width="714" height="420" viewBox="0 0 714 420" role="img" aria-label="Photo of a heap of shredded aluminium scrap under a blue sky">
    <defs>
      <linearGradient id="scrapSky" x1="0" y1="0" x2="0" y2="1">
        <stop offset="0" stop-color="#7aa3d4"/>
        <stop offset="0.38" stop-color="#b8cde4"/>
        <stop offset="0.5" stop-color="#a9adb2"/>
        <stop offset="0.8" stop-color="#7b7f85"/>
        <stop offset="1" stop-color="#5b5f64"/>
      </linearGradient>
    </defs>
    <path d="M415,0 C455,50 475,90 470,140 C466,175 455,185 458,215 C465,330 570,405 714,411 L714,0 Z" fill="url(#scrapSky)"/>
    <path d="M415,0 C455,50 475,90 470,140 C466,175 455,185 458,215 C465,330 570,405 714,411" fill="none" stroke="#22b14c" stroke-width="4"/>
  </svg>

  <h1 class="headline">Playing The Fair<br><span class="accent">Aluminium Recycling</span><br>Game For Good</h1>
  <p class="tagline">Our partnership with you is based<br>on common sense, mutual gain<br>and a better tomorrow</p>

  <div class="brand">
    <span class="brand-dot"></span>
    <span class="brand-name">Brightloop Co.</span>
  </div>

  <h2 class="section-title">YOU ARE HERE</h2>

  <h3 class="list-heading" style="top:354px">IT'S SIMPLE:</h3>
  <ul class="checklist steps">
    <li><svg class="tick"><use href="#tick"/></svg>We bring you a free bin</li>
    <li><svg class="tick"><use href="#tick"/></svg>You throw all and any aluminium waste into the bin - no need to super-clean it. Try to compact / squash the aluminium as much as possible</li>
    <li><svg class="tick"><use href="#tick"/></svg>We collect the bin at no charge</li>
    <li><svg class="tick"><use href="#tick"/></svg>We turn the aluminium waste into a desirable resource</li>
    <li><svg class="tick"><use href="#tick"/></svg>We pay you for however much of that resource your waste has generated - and give you a report on that, so you can see how good you are</li>
  </ul>

  <h3 class="list-heading" style="top:575px">EXAMPLES OF WHAT WE CAN TAKE:</h3>
  <ul class="checklist materials">
    <li><svg class="tick"><use href="#tick"/></svg>Used beverage cans - any</li>
    <li><svg class="tick"><use href="#tick"/></svg>Tinfoil-scrunched, crusty, burned or dirty</li>
    <li><svg class="tick"><use href="#tick"/></svg>Disposable BBQ roasting trays</li>
    <li><svg class="tick"><use href="#tick"/></svg>Aluminium takeaway containers</li>
    <li><svg class="tick"><use href="#tick"/></svg>Wine bottle screw tops (and collars - if you can get them off)</li>
  </ul>

  <div class="gallery">
    <div class="gallery-tile tile-scrap" role="img" aria-label="Photo of baled aluminium scrap in a yard"></div>
    <div class="gallery-tile tile-cans" role="img" aria-label="Photo of a pile of crushed beverage cans"></div>
    <div class="gallery-tile tile-trays" role="img" aria-label="Photo of disposable aluminium BBQ trays"></div>
    <div class="gallery-tile tile-caps" role="img" aria-label="Photo of colourful wine bottle screw caps"></div>
  </div>

  <svg class="footer-wave" width="714" height="130" viewBox="0 0 714 130" aria-hidden="true">
    <path d="M300,132 C400,62 550,31 716,29 L716,132 Z" fill="#1a5c32" stroke="#22b14c" stroke-width="3"/>
  </svg>

  <p class="call-label">CALL NOW!</p>
  <p class="call-number">026 555 0142</p>
  <p class="email">join@brightloopco.co.nz</p>
</main>
</body>
</html>
```